WordPress website design for wealth management company

A modern clean look website for a service company. This is mostly for information only, with a form to capture prospect contact information and schedule a 15 minutes call. There will be several static pages describe what services we offer, how we are different, and a blog section for posting articles and share resources. A section for client testimonials.
I want a website that is easy to understand and maintain. No proprietary plugins that cost extra. The main thing I need help is the visual layout / color palette that present a clean and professional look, select the suitable stock photos that convey the image of trust, professional, innovative, and high service.
Some websites with style I like include the following
- https://www.morvanhollis.com/
- https://www.tindlebrookplanningworks.com/
- https://quorvalfunds.com/private-equity-partners/
Also some websites in other industries with clean modern look
- https://plotwhirl.com/
- https://dabrix.com/
- https://www.fennelroost.com/
I want the end product to be a fully functional website that I can upload into web hosting service I use and I can easily add content and maintain myself in the future.

```html
<!DOCTYPE html>
<html lang="en">
<head>
<meta charset="utf-8">
<title>Harrowgate Wealth</title>
<link href="https://fonts.googleapis.com/css2?family=Oswald:wght@300;400;600&family=Montserrat:wght@400;500;600;700&family=Barlow:wght@400;500;600&display=swap" rel="stylesheet">
<style>
:root{
  --purple:#4b1a7a;
  --purple-deep:#3f1466;
  --purple-band:#4a1a78;
  --yellow:#f6b523;
  --yellow-soft:#f8c445;
  --ink:#1c1c1c;
  --text:#444;
  --muted:#777;
  --blush:#f8f3f3;
  --footer:#f1f1f8;
  --white:#fff;
}
*{box-sizing:border-box;margin:0;padding:0}
html,body{width:1200px;height:3886px;overflow:hidden}
body{position:relative;background:var(--white);font-family:"Montserrat",sans-serif;color:var(--text)}
.abs{position:absolute}
/* header */
.site-header{position:absolute;left:0;top:0;width:1200px;height:109px;background:var(--white)}
.brand{position:absolute;display:flex;align-items:center;gap:8px;font-family:"Montserrat",sans-serif;font-weight:600;color:var(--purple);letter-spacing:2px}
.brand-dot{border-radius:50%;background:var(--yellow)}
.header-brand{left:160px;top:38px;font-size:17px}
.header-brand .brand-dot{width:14px;height:14px}
.call{position:absolute;left:882px;top:12px;font-family:"Barlow",sans-serif;font-size:13px;color:var(--purple);font-weight:500;display:flex;align-items:center;gap:6px}
.call-icon{width:19px;height:19px;border-radius:50%;background:var(--yellow);display:flex;align-items:center;justify-content:center}
.main-nav{position:absolute;top:52px;left:474px;display:flex;gap:0;font-family:"Barlow",sans-serif;font-size:13px;color:#333}
.main-nav a{color:inherit;text-decoration:none;position:relative}
.main-nav a.active{font-weight:600}
.main-nav a.active::after{content:"";position:absolute;left:-14px;right:-14px;top:32px;height:2px;background:var(--purple)}
/* hero */
.hero{position:absolute;left:0;top:109px;width:1200px;height:600px}
.hero-copy{position:absolute;left:116px;top:150px;width:456px;height:456px;border-radius:50%;background:var(--yellow-soft);box-shadow:0 0 0 10px rgba(255,255,255,.85);text-align:center;padding-top:120px}
.hero-title{font-family:"Montserrat",sans-serif;font-weight:600;color:var(--purple);font-size:35px;line-height:48px}
.hero-text{font-size:16px;line-height:26px;color:#3a3a3a;margin-top:10px;padding:0 50px}
.btn{display:inline-block;border:2px solid var(--purple);border-radius:24px;color:var(--purple);font-weight:700;font-size:11px;text-transform:uppercase;text-align:center;background:transparent}
.hero-copy .btn{margin-top:26px;width:176px;height:44px;line-height:40px;font-size:12px}
.chev{position:absolute;top:378px}
/* shared heads */
.section-title{position:absolute;left:0;width:1200px;text-align:center;font-family:"Oswald",sans-serif;font-size:34px;color:var(--ink);letter-spacing:.5px}
.section-title b{font-weight:600}
.section-title span{font-weight:300}
.section-title::after{content:"";display:block;width:66px;height:3px;background:var(--purple);margin:6px auto 0}
.on-dark{color:var(--white)}
.on-dark::after{background:var(--white)}
/* photo placeholders */
.photo{position:absolute;overflow:hidden}
/* about */
.about-ring{position:absolute;left:128px;top:728px;width:448px;height:448px;border-radius:50%;border:6px solid var(--yellow);border-left-color:transparent;border-top-color:transparent;transform:rotate(-10deg)}
.about-photo{left:133px;top:740px;width:422px;height:422px;border-radius:50%;background:radial-gradient(circle at 60% 40%,#9c7350,#5a3a26 55%,#2e1e14)}
.about-copy{position:absolute;left:610px;top:800px;width:440px}
.about-copy h2,.contact-copy h2{font-family:"Oswald",sans-serif;font-size:34px;color:var(--ink);line-height:44px}
.about-copy h2 b,.contact-copy h2 b{font-weight:600}
.about-copy h2 span,.contact-copy h2 span{font-weight:300}
.about-copy h2::after,.contact-copy h2::after{content:"";display:block;width:86px;height:3px;background:var(--purple);margin-top:2px}
.lead{font-size:12.5px;line-height:21px;color:#222;font-weight:500;margin-top:10px}
.body{font-size:12px;line-height:22px;color:#555}
.about-copy .note{font-size:12.5px;line-height:20px;color:#222;margin-top:12px;width:360px}
.about-copy .btn{margin-top:24px;width:158px;height:40px;line-height:36px}
/* blogs */
.blogs{position:absolute;left:0;top:1254px;width:1200px;height:486px;background:var(--blush)}
.blog-card{position:absolute;top:1414px;width:432px;height:206px;background:var(--white);border:1px solid #ddd;box-shadow:0 2px 6px rgba(0,0,0,.08);overflow:hidden}
.blog-photo{left:0;top:0;width:200px;height:206px}
.blog-body{position:absolute;left:180px;top:0;width:252px;height:206px;background:var(--white);border-radius:60px 0 0 60px;padding:22px 16px 0 30px}
.date{font-size:12px;color:var(--yellow);display:flex;align-items:center;gap:5px}
.blog-body h3{font-size:15px;font-weight:700;color:#222;line-height:20px;margin-top:8px}
.blog-body p{font-size:12px;color:#888;line-height:18px;margin-top:10px}
.more{font-size:11.5px;font-weight:700;color:var(--purple);margin-top:10px;display:block;text-transform:uppercase}
.dots{position:absolute;left:565px;top:1652px;display:flex;gap:11px}
.dots i{width:11px;height:11px;border-radius:50%;background:#222;display:block}
.dots i.on{background:var(--yellow)}
/* testimonials */
.quote-card{position:absolute;top:1897px;width:436px;height:259px;border:2px solid var(--purple);border-radius:0 48px 0 48px;background:var(--white);padding:58px 32px 0 48px}
.quote-card p{font-size:12.5px;line-height:24.5px;color:#555}
.quote-card cite{display:block;font-style:normal;font-family:"Barlow",sans-serif;font-weight:600;font-size:14px;color:var(--purple);margin-top:14px}
.quote-mark{position:absolute;left:50px;top:-22px;width:60px;height:60px;border-radius:50%;background:var(--yellow);display:flex;align-items:center;justify-content:center}
/* resources */
.resources{position:absolute;left:0;top:2236px;width:1200px;height:609px;background:linear-gradient(90deg,#45186f,#521f85)}
.res-photo{top:2398px;width:302px;height:216px}
.res-card{position:absolute;top:2568px;width:268px;height:206px;background:var(--white);padding:20px 26px 0 26px}
.res-card.featured{border-bottom:5px solid var(--yellow)}
.pill{display:inline-block;background:var(--yellow);color:var(--white);font-size:10px;font-weight:600;padding:3px 14px;border-radius:10px}
.res-card h3{font-size:13.5px;font-weight:700;color:#222;line-height:19px;margin-top:12px}
.res-card p{font-size:12px;color:#555;line-height:19px;margin-top:8px}
.res-card .learn{font-size:11px;font-weight:600;color:var(--yellow);margin-top:8px;display:inline-block;border-bottom:1px solid var(--yellow);text-transform:uppercase}
/* contact */
.contact-copy{position:absolute;left:142px;top:2930px;width:440px}
.contact-copy .lead{font-size:12px;line-height:21px;margin-top:14px}
.field{position:absolute;left:142px;width:378px;height:37px;border:1.5px solid #999;font-size:12px;color:#999;padding:9px 16px;font-family:"Barlow",sans-serif}
.submit{position:absolute;left:142px;top:3349px;width:156px;height:38px;line-height:34px}
.contact-ring{position:absolute;left:620px;top:2910px;width:454px;height:454px;border-radius:50%;border:6px solid var(--yellow);border-right-color:transparent;border-top-color:transparent;transform:rotate(20deg)}
.contact-photo{left:640px;top:2928px;width:422px;height:422px;border-radius:50%;background:radial-gradient(circle at 45% 45%,#4a6a9a,#2b4470 55%,#1a2a48)}
/* footer */
.site-footer{position:absolute;left:0;top:3465px;width:1200px;height:421px;background:var(--footer)}
.footer-brand{left:132px;top:3600px;font-size:24px}
.footer-brand .brand-dot{width:18px;height:18px}
.socials{position:absolute;left:160px;top:3680px;display:flex;gap:12px}
.socials i{display:block;width:28px;height:28px;border-radius:50%;background:var(--purple)}
.vline{position:absolute;top:3473px;width:1px;height:302px;background:#c9c3da}
.fcol{position:absolute;top:3586px}
.fcol h4{font-family:"Barlow",sans-serif;font-weight:500;font-size:17px;color:#222;letter-spacing:.5px;border-left:2px solid var(--purple);padding-left:6px;margin-left:-8px}
.fcol ul{list-style:none;font-size:11.5px;color:#333;line-height:26px;margin-top:10px}
.contact-item{display:flex;gap:12px;font-size:11.5px;color:#333;line-height:18px;margin-top:14px}
.ci-icon{width:28px;height:28px;border-radius:50%;background:var(--purple);display:flex;align-items:center;justify-content:center;flex:none}
.hours{font-size:11.5px;color:#333;line-height:18.5px;margin-top:10px}
.hours div{display:flex}
.hours span{width:70px}
.copyright{position:absolute;left:0;top:3842px;width:1200px;border-top:1px solid #bbb;text-align:center;font-size:11px;color:#333;padding-top:16px}
</style>
</head>
<body>

<header class="site-header">
  <div class="brand header-brand"><span class="brand-dot"></span>HARROWGATE WEALTH</div>
  <div class="call"><span class="call-icon"><svg width="10" height="10" viewBox="0 0 24 24"><path fill="#fff" d="M6.6 10.8a15 15 0 006.6 6.6l2.2-2.2a1 1 0 011-.25 11.4 11.4 0 003.6.6 1 1 0 011 1V20a1 1 0 01-1 1A17 17 0 013 4a1 1 0 011-1h3.5a1 1 0 011 1c0 1.25.2 2.45.6 3.6a1 1 0 01-.25 1z"/></svg></span>Call Us Today (203) 555-0148</div>
  <nav class="main-nav">
    <a class="active" href="#" style="margin-right:48px">Home</a>
    <a href="#" style="margin-right:56px">About Us</a>
    <a href="#" style="margin-right:56px">Blogs</a>
    <a href="#" style="margin-right:56px">Testimonials</a>
    <a href="#" style="margin-right:56px">Resouces</a>
    <a href="#">Contact Us</a>
  </nav>
</header>

<section class="hero">
  <svg class="abs" style="left:0;top:0" width="1200" height="600" role="img" aria-label="Photo of a couple sitting together on a boat deck looking out over sunlit water">
    <defs><linearGradient id="heroSky" x1="0" y1="0" x2="1" y2="1"><stop offset="0" stop-color="#e9d7bd"/><stop offset=".45" stop-color="#b9b3ad"/><stop offset=".75" stop-color="#6f7784"/><stop offset="1" stop-color="#4e5663"/></linearGradient></defs>
    <path d="M0 0H1200V500Q760 640 430 590Q180 555 0 500Z" fill="url(#heroSky)"/>
  </svg>
  <svg class="chev" style="left:48px" width="26" height="50" viewBox="0 0 26 50"><path d="M22 3L4 25l18 22" fill="none" stroke="#fff" stroke-width="3"/></svg>
  <svg class="chev" style="left:1122px" width="26" height="50" viewBox="0 0 26 50"><path d="M4 3l18 22L4 47" fill="none" stroke="#fff" stroke-width="3"/></svg>
</section>
<div class="hero-copy">
  <h1 class="hero-title">WELCOME TO<br>HARROWGATE WEALTH</h1>
  <p class="hero-text">Lorem Ipsum has been the industry's standard dummy text ever since the 1500s.</p>
  <span class="btn">Chat with us</span>
</div>

<section>
  <div class="about-ring"></div>
  <div class="photo about-photo" role="img" aria-label="Photo of a smiling older couple embracing in warm evening light"></div>
  <div class="about-copy">
    <h2><b>ABOUT</b> <span>US</span></h2>
    <p class="lead">Lorem ipsum dolor sit amet, consectetur adipiscing elit, sed do eiusmod tempor incididunt ut labore et dolore.</p>
    <p class="body">magna aliqua. Ut enim ad minim veniam, quis nostrud exercitation ullamco laboris nisi ut aliquip ex ea commodo consequat. Duis aute irure dolor in reprehenderit in voluptate velit esse cillum dolore eu fugiat nulla pariatur. Excepteur sint occaecat cupidatat non proident, sunt in</p>
    <p class="note">The industry's standard dummy text ever since the 1500s. when an unknown.</p>
    <span class="btn">Read more</span>
  </div>
</section>

<section class="blogs"></section>
<h2 class="section-title" style="top:1318px"><b>FEATURED</b> <span>BLOGS</span></h2>
<article class="blog-card" style="left:154px">
  <div class="photo blog-photo" role="img" aria-label="Photo of an older couple standing in front of their house" style="background:linear-gradient(135deg,#8a9aa6,#c2c0b4 50%,#5f6b4e)"></div>
  <div class="blog-body">
    <div class="date"><svg width="12" height="12" viewBox="0 0 12 12"><rect x="1" y="2" width="10" height="9" fill="none" stroke="#f6b523"/><path d="M1 5h10" stroke="#f6b523"/></svg>10 DEC 2018</div>
    <h3>Pellentesque faucibus Ut accumsa Donec</h3>
    <p>Duis quam Nam eget lacus Aliquam erat volutpat Quisque dignissim congue leoMauris vel lacus</p>
    <span class="more">Read more</span>
  </div>
</article>
<article class="blog-card" style="left:613px">
  <div class="photo blog-photo" role="img" aria-label="Photo of a smiling woman in a meeting at a bright office" style="background:linear-gradient(135deg,#c8ccd0,#d9b9a6 50%,#7b8a96)"></div>
  <div class="blog-body">
    <div class="date"><svg width="12" height="12" viewBox="0 0 12 12"><rect x="1" y="2" width="10" height="9" fill="none" stroke="#f6b523"/><path d="M1 5h10" stroke="#f6b523"/></svg>10 DEC 2018</div>
    <h3>Pellentesque faucibus Ut accumsa Donec</h3>
    <p>Duis quam Nam eget lacus Aliquam erat volutpat Quisque dignissim congue leoMauris vel lacus</p>
    <span class="more">Read more</span>
  </div>
</article>
<div class="dots"><i></i><i class="on"></i><i></i></div>

<h2 class="section-title" style="top:1789px"><b>TESTIMONIALS</b></h2>
<svg class="abs" style="left:100px;top:2006px" width="22" height="34" viewBox="0 0 22 34"><path d="M18 3L5 17l13 14" fill="none" stroke="#555" stroke-width="3"/></svg>
<svg class="abs" style="left:1085px;top:2006px" width="22" height="34" viewBox="0 0 22 34"><path d="M4 3l13 14L4 31" fill="none" stroke="#555" stroke-width="3"/></svg>
<blockquote class="quote-card" style="left:157px">
  <span class="quote-mark"><svg width="30" height="22" viewBox="0 0 30 22"><path fill="#fff" d="M0 12Q0 2 10 0v4Q5 6 5 10h6v12H0zM17 12q0-10 10-12v4q-5 2-5 6h6v12H17z"/></svg></span>
  <p>My family and I are so appreciative of all the help you've provided to us and for being so patient and flexible with all we've been through and the changes we've thrown your way last minute. I trust this company explicitly to always send us the right caregiver</p>
  <cite>Delia R.(Fairview)</cite>
</blockquote>
<blockquote class="quote-card" style="left:615px">
  <span class="quote-mark"><svg width="30" height="22" viewBox="0 0 30 22"><path fill="#fff" d="M0 12Q0 2 10 0v4Q5 6 5 10h6v12H0zM17 12q0-10 10-12v4q-5 2-5 6h6v12H17z"/></svg></span>
  <p>My 93 year-old mom experiences Sundowing and insisted on remaining in her home. Without the live-in care provided by Evenbrook Aides, I don't know how we could have managed it. The aides were well trained and very professional. I would recommend them highly.</p>
  <cite>- Tobin (Westmere)</cite>
</blockquote>

<section class="resources"></section>
<h2 class="section-title on-dark" style="top:2292px"><span>OUR</span> <b>RESOURCES</b></h2>
<div class="photo res-photo" style="left:133px;background:linear-gradient(135deg,#dfe3e6,#9aa4ad 55%,#3c4250)" role="img" aria-label="Photo of two colleagues reviewing documents at a desk"></div>
<div class="photo res-photo" style="left:456px;background:linear-gradient(135deg,#b9b6b0,#8a8580 50%,#3d3b3c)" role="img" aria-label="Photo of an older couple meeting with an advisor"></div>
<div class="photo res-photo" style="left:779px;background:linear-gradient(135deg,#d79a4e,#9b5a34 50%,#4a2d22)" role="img" aria-label="Photo of a smiling couple outdoors at sunset"></div>
<article class="res-card" style="left:151px">
  <span class="pill">Mar 16, 2023</span>
  <h3>Keep your Loved Ones Safe at home</h3>
  <p>Sed ut perspiciatis unde omnis iste natus error sit voluptatem accusantium doloremque</p>
  <span class="learn">Learn more</span>
</article>
<article class="res-card featured" style="left:476px">
  <span class="pill">Mar 16, 2023</span>
  <h3>Safeguarding Against the Coronavirus COVID-19</h3>
  <p>Sed ut perspiciatis unde omnis iste natus error sit voluptatem accusantium doloremque</p>
  <span class="learn">Learn more</span>
</article>
<article class="res-card" style="left:799px">
  <span class="pill">Jan 14, 2023</span>
  <h3>Why Hire a Home Care Company</h3>
  <p>Sed ut perspiciatis unde omnis iste natus error sit voluptatem accusantium doloremque</p>
  <span class="learn">Learn more</span>
</article>

<section>
  <div class="contact-copy">
    <h2><b>CONTACT</b> <span>US</span></h2>
    <p class="lead">Lorem ipsum dolor sit amet, consectetur adipiscing elit, sed do eiusmod tempor incididunt ut labore et dolore.</p>
  </div>
  <div class="field" style="top:3049px">First Name</div>
  <div class="field" style="top:3098px">Last &nbsp;Name</div>
  <div class="field" style="top:3148px">Email address</div>
  <div class="field" style="top:3197px">Phone</div>
  <div class="field" style="top:3245px;height:86px">Message</div>
  <span class="btn submit">Submit</span>
  <div class="contact-ring"></div>
  <div class="photo contact-photo" role="img" aria-label="Photo of a smiling advisor holding a tablet"></div>
</section>

<footer class="site-footer"></footer>
<div class="brand footer-brand"><span class="brand-dot"></span>HARROWGATE</div>
<div class="socials" aria-label="Social links"><i></i><i></i><i></i></div>
<div class="vline" style="left:377px"></div>
<div class="vline" style="left:557px"></div>
<div class="vline" style="left:859px"></div>
<div class="fcol" style="left:404px">
  <h4>NAVIGATION</h4>
  <ul><li>Home</li><li>About Us</li><li>Lawyers</li><li>Practice Areas</li><li>Contact Us</li></ul>
</div>
<div class="fcol" style="left:577px">
  <h4>CONTACT US</h4>
  <div class="contact-item"><span class="ci-icon"><svg width="13" height="13" viewBox="0 0 24 24"><path fill="#fff" d="M6.6 10.8a15 15 0 006.6 6.6l2.2-2.2a1 1 0 011-.25 11.4 11.4 0 003.6.6 1 1 0 011 1V20a1 1 0 01-1 1A17 17 0 013 4a1 1 0 011-1h3.5a1 1 0 011 1c0 1.25.2 2.45.6 3.6a1 1 0 01-.25 1z"/></svg></span><div>Phone<br>123-456-7890</div></div>
  <div class="contact-item"><span class="ci-icon"><svg width="13" height="10" viewBox="0 0 13 10"><rect x=".5" y=".5" width="12" height="9" fill="none" stroke="#fff"/><path d="M.5.5l6 5 6-5" fill="none" stroke="#fff"/></svg></span><div>Email<br>hello@harrowgatewealth.example</div></div>
  <div class="contact-item"><span class="ci-icon"><svg width="11" height="14" viewBox="0 0 11 14"><path fill="#fff" d="M5.5 0A5.5 5.5 0 000 5.5C0 9.5 5.5 14 5.5 14S11 9.5 11 5.5A5.5 5.5 0 005.5 0zm0 7.5a2 2 0 110-4 2 2 0 010 4z"/></svg></span><div>Address<br>218 Larkspur Avenue, Brindlewood 4021</div></div>
</div>
<div class="fcol" style="left:882px">
  <h4>WORKING HOURS</h4>
  <div class="hours">
    <div><span>Monday</span>9:00am - 5:00pm</div>
    <div><span>Tuesday</span>9:00am - 5:00pm</div>
    <div><span style="width:94px">Wednesday</span>9:00am - 5:00pm</div>
    <div><span>Thursday</span>9:00am - 5:00pm</div>
    <div><span style="width:48px">Friday</span>9:00am - 5:00pm</div>
    <div><span>Saturday</span>10:00am - 3:00pm</div>
    <div><span>Sunday</span>Closed</div>
  </div>
</div>
<div class="copyright">© 2023 HARROWGATE WEALTH. ALL RIGHTS RESERVED</div>

</body>
</html>
```